175th Anniversary of Family Owned Funeral Home Pole Banners

We are family owned and operated funeral home in the Greater Cincinnati area and operate 3 funeral homes and a cremation center and we will be celebrating our 175th anniversary in 2015. The communities we serve look to us as leaders in the community and we are very well recognized. In preparation for next year, part of our planning includes placing pole banners in our local communities and our funeral home parking areas. The banner dimensions will be 30 x 60. We need for the banners to display a great message of tradition and excellence. Our website is www.brannockvelder.com I have uploaded an example of a pole banner as well as our logo(s).
Updates
Original artwork has been uploaded if needed.
Industry/Entity Type
Funeral Home

```html
<!DOCTYPE html>
<html lang="en">
<head>
<meta charset="utf-8">
<title>Brannock Velder – 175th Anniversary Pole Banner</title>
<link rel="stylesheet" href="https://fonts.googleapis.com/css2?family=Open+Sans:wght@400;600;700&display=swap">
<style>
  :root {
    --page-bg: #d9d9d9;
    --ink-black: #161616;
    --panel-black: #232323;
    --silver-light: #f2f2f2;
    --silver-mid: #b9b9b9;
    --silver-dark: #8a8a8a;
    --brand-red: #c8101a;
    --brand-red-dark: #8e0a10;
    --text-white: #ffffff;
    --text-soft: #e6e6e6;
    --accent-yellow: #f3e33a;
    --arrow-tint: #f0a07a;
  }
  html, body {
    margin: 0;
    width: 1200px;
    height: 1051px;
    overflow: hidden;
    background: var(--page-bg);
    font-family: "Open Sans", Arial, sans-serif;
  }
  .banner {
    position: absolute;
    left: 410px;
    top: 25px;
    width: 380px;
    height: 1000px;
    overflow: hidden;
    background: var(--panel-black);
    box-shadow: 0 6px 24px rgba(0,0,0,0.25);
  }
  .banner > svg { position: absolute; left: 0; top: 0; }
  .photo-memorial { z-index: 1; }
  .banner-shapes { z-index: 2; }
  .brand {
    position: absolute;
    z-index: 3;
    left: 34px;
    top: 34px;
    color: var(--text-white);
    display: flex;
    align-items: center;
    gap: 10px;
  }
  .brand-dot {
    width: 18px; height: 18px;
    border-radius: 50%;
    background: var(--text-white);
  }
  .brand-name {
    font-weight: 600;
    font-size: 25px;
    line-height: 1;
  }
  .brand-tagline {
    position: absolute;
    z-index: 3;
    left: 34px;
    top: 68px;
    color: var(--text-soft);
    font-size: 12px;
  }
  .anniversary {
    position: absolute;
    z-index: 3;
    left: 26px;
    top: 600px;
    width: 340px;
    color: var(--text-white);
  }
  .anniversary-title {
    margin: 0;
    font-weight: 700;
    font-size: 30px;
    line-height: 1.22;
    text-transform: uppercase;
    letter-spacing: 0.2px;
  }
  .anniversary-title sup { font-size: 16px; vertical-align: 11px; }
  .anniversary-lede {
    margin: 12px 0 0;
    font-size: 13.5px;
    line-height: 1.35;
    font-style: italic;
    font-weight: 600;
  }
  .anniversary-lede .highlight { color: var(--accent-yellow); }
  .options {
    list-style: none;
    margin: 16px 0 0;
    padding: 0;
    font-size: 13px;
  }
  .options li {
    display: flex;
    align-items: center;
    gap: 8px;
    margin-bottom: 9px;
  }
  .tick-icon { flex: none; }
  .footer-info {
    position: absolute;
    z-index: 3;
    left: 24px;
    bottom: 24px;
    color: var(--text-white);
  }
  .footer-lead { font-size: 11.5px; }
  .footer-url {
    display: flex;
    align-items: center;
    gap: 8px;
    font-size: 16px;
    font-weight: 700;
  }
  .footer-arrows { flex: none; }
  .footer-brand {
    position: absolute;
    z-index: 3;
    right: 16px;
    bottom: 30px;
    color: var(--text-white);
    font-size: 10px;
    font-weight: 600;
  }
</style>
</head>
<body>
<div class="banner">
  <svg class="photo-memorial" width="380" height="1000" role="img" aria-label="Photograph of pallbearers in dark suits carrying a casket topped with red and white roses">
    <defs>
      <linearGradient id="photoTones" x1="0" y1="0" x2="1" y2="1">
        <stop offset="0" stop-color="#2b3038"/>
        <stop offset="0.35" stop-color="#5a1a1c"/>
        <stop offset="0.6" stop-color="#b0141c"/>
        <stop offset="0.8" stop-color="#3f6a2a"/>
        <stop offset="1" stop-color="#b56a4a"/>
      </linearGradient>
    </defs>
    <rect x="0" y="120" width="380" height="500" fill="url(#photoTones)"/>
  </svg>

  <svg class="banner-shapes" width="380" height="1000" aria-hidden="true">
    <defs>
      <linearGradient id="silverSweep" x1="0" y1="0" x2="1" y2="0">
        <stop offset="0" stop-color="var(--silver-dark)"/>
        <stop offset="0.5" stop-color="var(--silver-light)"/>
        <stop offset="1" stop-color="var(--silver-mid)"/>
      </linearGradient>
      <linearGradient id="redFade" x1="0" y1="0" x2="0" y2="1">
        <stop offset="0" stop-color="var(--brand-red)"/>
        <stop offset="1" stop-color="var(--brand-red-dark)"/>
      </linearGradient>
      <linearGradient id="blackFade" x1="0" y1="0" x2="0" y2="1">
        <stop offset="0" stop-color="#0e0e0e"/>
        <stop offset="1" stop-color="#333333"/>
      </linearGradient>
    </defs>
    <path d="M0,0 H380 V118 Q250,150 0,190 Z" fill="url(#silverSweep)"/>
    <path d="M0,0 H380 V86 Q250,132 0,160 Z" fill="var(--ink-black)"/>
    <path d="M0,500 Q150,555 380,565 V1000 H0 Z" fill="url(#silverSweep)"/>
    <path d="M0,528 Q170,580 380,590 V1000 H0 Z" fill="url(#blackFade)"/>
    <path d="M0,900 Q220,880 380,835 V1000 H0 Z" fill="url(#silverSweep)"/>
    <path d="M0,925 Q230,905 380,860 V1000 H0 Z" fill="url(#redFade)"/>
  </svg>

  <div class="brand"><span class="brand-dot"></span><span class="brand-name">Brannock Velder</span></div>
  <div class="brand-tagline">Family Funeral Homes &amp; Cremation Center</div>

  <section class="anniversary">
    <h1 class="anniversary-title">Celebrating<br>175<sup>TH</sup> Anniversary</h1>
    <p class="anniversary-lede">Sed ut perspiciatis iste natus error voluptatem accusantium <span class="highlight">doloremque laudantium</span></p>
    <ul class="options">
      <li><svg class="tick-icon" width="14" height="14" viewBox="0 0 14 14" aria-hidden="true"><circle cx="7" cy="7" r="7" fill="#fff"/><path d="M3.8,7.2 L6,9.3 L10.2,4.8" fill="none" stroke="#222" stroke-width="1.8"/></svg>Option One text goes here</li>
      <li><svg class="tick-icon" width="14" height="14" viewBox="0 0 14 14" aria-hidden="true"><circle cx="7" cy="7" r="7" fill="#fff"/><path d="M3.8,7.2 L6,9.3 L10.2,4.8" fill="none" stroke="#222" stroke-width="1.8"/></svg>Option Two text goes here</li>
      <li><svg class="tick-icon" width="14" height="14" viewBox="0 0 14 14" aria-hidden="true"><circle cx="7" cy="7" r="7" fill="#fff"/><path d="M3.8,7.2 L6,9.3 L10.2,4.8" fill="none" stroke="#222" stroke-width="1.8"/></svg>Option Three text goes here</li>
    </ul>
  </section>

  <div class="footer-info">
    <div class="footer-lead">for more details visit our website</div>
    <div class="footer-url">www.brannockvelder.com
      <svg class="footer-arrows" width="26" height="12" viewBox="0 0 26 12" aria-hidden="true">
        <path d="M0,0 L6,6 L0,12 Z M9,0 L15,6 L9,12 Z M18,0 L24,6 L18,12 Z" fill="var(--arrow-tint)"/>
      </svg>
    </div>
  </div>
  <div class="footer-brand">Brannock Velder</div>
</div>
</body>
</html>
```